CLAIM BARRIER PLAN

I'm virtually ready to launch my site, but I have a number of edits and modifications that need to be implemented. More importantly, I'm always looking to improve my site, particularly now that I am making my proverbial "FIRST IMPRESSION." Thus, I'm willing to see if there is someone who can add creativity and perhaps improve what I already have, particularly on the All Important Front Page.

Need extra days to review

```html
<!DOCTYPE html>
<html lang="en">
<head>
<meta charset="utf-8">
<title>Claim Barrier Plan</title>
<link rel="stylesheet" href="https://fonts.googleapis.com/css2?family=Poppins:ital,wght@0,400;0,500;0,600;0,700;1,500&display=swap">
<style>
:root{
  --red:#a51c38;
  --red-deep:#8c1630;
  --navy:#0e2148;
  --ink:#3a3a3a;
  --white:#ffffff;
  --field:#eeeeee;
  --black:#000000;
  --teal:#0d6e6e;
}
*{box-sizing:border-box;margin:0;padding:0}
html,body{width:1200px;height:3743px;overflow:hidden}
body{font-family:"Poppins",sans-serif;color:var(--ink);background:var(--white);position:relative}
section,header,footer{position:relative;width:1200px;overflow:hidden}
.abs{position:absolute}

/* header */
.site-header{height:80px;background:var(--white)}
.brand{left:77px;top:8px;display:flex;align-items:center;gap:10px}
.brand-dot{width:64px;height:64px;border-radius:50%;background:var(--navy)}
.brand-name{font-weight:600;font-size:13px;color:var(--navy);line-height:1.2;width:80px}
.main-nav{left:266px;top:28px;display:flex;gap:0}
.main-nav a{font-size:19px;font-weight:500;color:var(--black);text-decoration:none;margin-right:44px}
.header-phone{left:926px;top:14px;display:flex;align-items:center;gap:16px;font-size:19px;font-weight:500;color:var(--black)}
.phone-ring{width:46px;height:46px;border:2px solid var(--red);border-radius:50%;display:flex;align-items:center;justify-content:center}

/* hero */
.hero{height:562px;background:linear-gradient(100deg,#1d1410 0%,#3a2519 35%,#5a3d27 60%,#2a1d15 100%)}
.hero-title{left:77px;top:120px;font-size:50px;font-weight:600;color:var(--white);letter-spacing:1px}
.hero-copy{left:77px;top:204px;width:650px;font-size:17px;line-height:20px;color:var(--white)}
.hero-copy p+p{margin-top:8px}
.btn{display:flex;align-items:center;justify-content:center;border-radius:24px;font-size:17px;font-weight:500;color:var(--white);text-decoration:none}
.btn-red{background:var(--red)}
.btn-outline{border:2px solid var(--white)}

/* about */
.about{height:529px}
.about-photo{left:173px;top:109px;width:320px;height:320px;border-radius:50%;background:radial-gradient(circle at 50% 45%,#6a4a35,#2b1c14)}
.section-title{font-size:38px;font-weight:700;color:var(--navy)}
.about-title{left:540px;top:108px}
.about-copy{left:540px;top:195px;width:510px;font-size:12.5px;line-height:18px}
.about-copy p+p{margin-top:34px}

/* services */
.services{height:729px;background:linear-gradient(160deg,#b4223f 0%,#9e1a35 50%,#8a1730 100%)}
.service{width:300px;text-align:center;color:var(--white)}
.service-photo{width:146px;height:146px;border-radius:50%;margin:0 auto}
.service-name{font-size:19px;font-weight:600;line-height:21px;margin-top:12px}
.service-text{font-size:10px;line-height:14px;margin-top:10px;padding:0 12px}

/* case study */
.case{height:531px}
.case-title{left:134px;top:120px}
.case-copy{left:134px;top:192px;width:550px;font-size:12.5px;line-height:18px}
.case-photo{left:720px;top:75px;width:320px;height:320px;border-radius:50%;background:radial-gradient(circle at 45% 50%,#d8d2c4,#8e8878 70%,#5c6a55)}
.case-quote{left:720px;top:410px;width:340px;text-align:center;font-style:italic;font-weight:500;font-size:13px;line-height:18px;color:#555}
.case-author{left:720px;top:463px;width:340px;text-align:center;font-weight:600;font-size:13px;color:var(--navy)}

/* faq */
.faq{height:453px;background:var(--red)}
.faq-title{left:0;top:52px;width:1150px;text-align:center;font-size:28px;font-weight:600;color:var(--white)}
.faq-item{width:426px;height:62px;border:2px solid var(--white);border-radius:12px;display:flex;align-items:center;justify-content:space-between;padding:0 22px 0 16px;color:var(--white);font-size:11px;font-weight:500;line-height:14px}
.faq-arrow{width:24px;height:24px;border-radius:50%;background:var(--white);display:flex;align-items:center;justify-content:center;flex:none}

/* contact */
.contact{height:433px}
.contact-title{left:0;top:52px;width:1240px;text-align:center}
.field{background:var(--field);border-radius:20px;color:#8a8a8a;font-size:14px;padding:10px 12px}
.submit{left:497px;top:346px;width:250px;height:45px}

/* footer */
.site-footer{height:426px;background:var(--black);color:var(--white)}
.foot-brand{left:117px;top:114px;width:106px;height:106px;border-radius:50%;border:3px solid var(--red);background:var(--navy);display:flex;align-items:center;justify-content:center;text-align:center;font-size:12px;font-weight:600;line-height:15px}
.social{top:258px;width:18px;height:18px;border-radius:50%;background:var(--white)}
.foot-head{top:112px;font-size:17px;font-weight:500}
.foot-link{left:478px;font-size:17px}
.foot-info{left:832px;display:flex;align-items:flex-start;gap:12px;font-size:14px;line-height:19px}
.foot-icon{width:32px;height:32px;border:2px solid var(--red);border-radius:50%;display:flex;align-items:center;justify-content:center;flex:none}
.foot-rule{left:190px;top:333px;width:882px;height:1px;background:var(--red)}
.copyright{left:0;top:354px;width:1260px;text-align:center;font-size:14px}
</style>
</head>
<body>

<header class="site-header">
  <div class="brand abs"><span class="brand-dot"></span><span class="brand-name">Claim Barrier Plan</span></div>
  <nav class="main-nav abs"><a href="#">HOME</a><a href="#">ABOUT</a><a href="#">SERVICES</a><a href="#">FAQs</a><a href="#">CONTACT</a></nav>
  <div class="header-phone abs">
    <span class="phone-ring"><svg width="22" height="22" viewBox="0 0 24 24"><path fill="#a51c38" d="M6.6 10.8a15 15 0 0 0 6.6 6.6l2.2-2.2a1 1 0 0 1 1-.25 11.4 11.4 0 0 0 3.6.57 1 1 0 0 1 1 1V20a1 1 0 0 1-1 1A17 17 0 0 1 3 4a1 1 0 0 1 1-1h3.5a1 1 0 0 1 1 1c0 1.25.2 2.45.57 3.6a1 1 0 0 1-.25 1z"/></svg></span>
    480.555.0142
  </div>
</header>

<section class="hero" role="img" aria-label="Courtroom interior with a lawyer standing near the bench in warm window light">
  <h1 class="hero-title abs">BLOCK THE CLAIM</h1>
  <div class="hero-copy abs">
    <p>BUSINESS OWNERS: Claim Barrier Plan (CBP) Is An Extremely Affordable Legal Service Plan (As Little As $8.00 Per Month) That INSULATES Business Owners From Unwarranted LEGAL CLAIMS And Expensive LAWSUITS.</p>
    <p>Plan Uses Local, Experienced, Quality Attorneys Who Focus On PROBLEM PREVENTION Using Proprietary Tools Available Only To CBP Members. Contact Us For A Free Consultation And Receive A FREE OVERVIEW Of Your Business To See If You Are Truly Insulated From Legal Claims.</p>
  </div>
  <a class="btn btn-red abs" href="#" style="left:77px;top:394px;width:147px;height:44px">LEARN MORE</a>
  <a class="btn btn-outline abs" href="#" style="left:243px;top:394px;width:238px;height:44px">FREE CONSULTATION</a>
</section>

<section class="about">
  <div class="about-photo abs" role="img" aria-label="Attorney in a robe on the phone holding papers in a library office"></div>
  <h2 class="section-title about-title abs">ABOUT US</h2>
  <div class="about-copy abs">
    <p>CBP is a group of attorney and legal assistants with many years of experience in litigation, who are devoted to PREVENTING LEGAL CLAIMS and COSTLY LAWSUITS through a variety of FREE and VERY AFFORDABLE services</p>
    <p>In our vast experience with commercial litigation, we believe that a very large percentage of litigation cases hinge on "he said / she said" issues. By using CBP's services, we believe we can INSULATE you and your business from all such issues, which will MINIMIZE your EXPOSURE to LEGAL CLAIMS and LAWSUITS.</p>
  </div>
  <a class="btn btn-red abs" href="#" style="left:538px;top:385px;width:147px;height:44px">LEARN MORE</a>
</section>

<section class="services" aria-label="Services">
  <div class="service abs" style="left:96px;top:64px">
    <div class="service-photo" role="img" aria-label="Scales of justice beside a gesturing hand" style="background:radial-gradient(circle,#8a6a50,#3a2a20)"></div>
    <h3 class="service-name">FREE INITIAL<br>CONSULTATION</h3>
    <p class="service-text">As a prospective Claim Barrier Plan ("CBP") member, we urge you to schedule an initial consultation with us – at no charge – where we will go over each of the services in detail, and offer an overview of your business formation at no charge.</p>
  </div>
  <div class="service abs" style="left:449px;top:64px">
    <div class="service-photo" role="img" aria-label="Gavel resting on a contract" style="background:radial-gradient(circle,#b08a60,#4a3020)"></div>
    <h3 class="service-name">PROPRIETARY CONTRACT<br>LANGUAGE</h3>
    <p class="service-text">As a prospective Claim Barrier Plan ("CBP") member, we urge you to schedule an initial consultation with us – at no charge – where we will go over each of the services in detail, and offer an overview of your business formation at no charge.</p>
  </div>
  <div class="service abs" style="left:806px;top:64px">
    <div class="service-photo" role="img" aria-label="Hand touching a blue digital consultation screen" style="background:radial-gradient(circle,#5a8ad0,#13306a)"></div>
    <h3 class="service-name">FREE<br>CONSULTATION</h3>
    <p class="service-text">As a prospective Claim Barrier Plan ("CBP") member, we urge you to schedule an initial consultation with us – at no charge – where we will go over each of the services in detail, and offer an overview of your business formation at no charge.</p>
  </div>
  <div class="service abs" style="left:82px;top:398px">
    <div class="service-photo" role="img" aria-label="Attorney reviewing a letter at a desk" style="background:radial-gradient(circle,#c8b8a8,#6a5a4c)"></div>
    <h3 class="service-name">FREE ATTORNEY<br>LETTERS</h3>
    <p class="service-text">As a prospective Claim Barrier Plan ("CBP") member, we urge you to schedule an initial consultation with us – at no charge – where we will go over each of the services in detail, and offer an overview of your business formation at no charge.</p>
  </div>
  <div class="service abs" style="left:447px;top:398px">
    <div class="service-photo" role="img" aria-label="Gavel on top of banknotes" style="background:radial-gradient(circle,#9a8a70,#4a3a2a)"></div>
    <h3 class="service-name">LITIGATION<br>DISCOUNTS</h3>
    <p class="service-text">As a prospective Claim Barrier Plan ("CBP") member, we urge you to schedule an initial consultation with us – at no charge – where we will go over each of the services in detail, and offer an overview of your business formation at no charge.</p>
  </div>
  <div class="service abs" style="left:815px;top:398px">
    <div class="service-photo" role="img" aria-label="Scales of justice and gavel on a desk" style="background:radial-gradient(circle,#d8d0c8,#6a5a50)"></div>
    <h3 class="service-name" style="margin-top:19px">COLLECTIONS</h3>
    <p class="service-text" style="margin-top:24px">As a prospective Claim Barrier Plan ("CBP") member, we urge you to schedule an initial consultation with us – at no charge – where we will go over each of the services in detail, and offer an overview of your business formation at no charge.</p>
  </div>
</section>

<section class="case">
  <h2 class="section-title case-title abs">CASE STUDY</h2>
  <p class="case-copy abs">A homebuilding company was sued by a former employee who claimed to have been promised a more favorable sales area, which claim was disputed by the homebuilder. There was no evidence that such a promise had been made, other than the plaintiff's oral testimony. The company had the case dismissed, but spent $10,000 defending the case. And even though it was awarded its attorney's fees, the plaintiff proved uncollectible. Had the company been an CBP member, the case likely would never have been filed. Call for your FREE CONSULTATION and let us show you why the plaintiff likely would not have found a contingency attorney (as was the case) or been able to pay an attorney on an hourly basis. In short, by using CBP's services, the plaintiff's claim would not have been filed.</p>
  <div class="case-photo abs" role="img" aria-label="Close-up of a banknote portrait wearing a face mask"></div>
  <p class="case-quote abs">An OUNCE of PREVENTION is<br>worth a POUND of CURE.</p>
  <p class="case-author abs">Elias Marlowe</p>
</section>

<section class="faq">
  <h2 class="faq-title abs">FREQUENTLY ASKED QUESTIONS</h2>
  <div class="faq-item abs" style="left:137px;top:145px"><span>Why should I be concerned about legal claims?</span><span class="faq-arrow"><svg width="14" height="14" viewBox="0 0 14 14"><path d="M2 7h9M7 3l4 4-4 4" stroke="#0d6e6e" stroke-width="2.4" fill="none"/></svg></span></div>
  <div class="faq-item abs" style="left:604px;top:145px"><span>Provide more details about the value of CBP's<br>contract language.</span><span class="faq-arrow"><svg width="14" height="14" viewBox="0 0 14 14"><path d="M2 7h9M7 3l4 4-4 4" stroke="#0d6e6e" stroke-width="2.4" fill="none"/></svg></span></div>
  <div class="faq-item abs" style="left:140px;top:232px"><span>If I'm a contractor, for example, how can an CBP<br>membership minimize legal claims against my business?</span><span class="faq-arrow"><svg width="14" height="14" viewBox="0 0 14 14"><path d="M2 7h9M7 3l4 4-4 4" stroke="#0d6e6e" stroke-width="2.4" fill="none"/></svg></span></div>
  <div class="faq-item abs" style="left:607px;top:232px"><span>What does an CBP membership cost?</span><span class="faq-arrow"><svg width="14" height="14" viewBox="0 0 14 14"><path d="M2 7h9M7 3l4 4-4 4" stroke="#0d6e6e" stroke-width="2.4" fill="none"/></svg></span></div>
  <div class="faq-item abs" style="left:141px;top:320px"><span>Do you have a Referral Program?</span><span class="faq-arrow"><svg width="14" height="14" viewBox="0 0 14 14"><path d="M2 7h9M7 3l4 4-4 4" stroke="#0d6e6e" stroke-width="2.4" fill="none"/></svg></span></div>
  <div class="faq-item abs" style="left:609px;top:320px"><span>Do you have a Referral Program?</span><span class="faq-arrow"><svg width="14" height="14" viewBox="0 0 14 14"><path d="M2 7h9M7 3l4 4-4 4" stroke="#0d6e6e" stroke-width="2.4" fill="none"/></svg></span></div>
</section>

<section class="contact">
  <h2 class="section-title contact-title abs">CONTACT US</h2>
  <div class="field abs" style="left:299px;top:139px;width:192px;height:38px">Name</div>
  <div class="field abs" style="left:526px;top:139px;width:192px;height:38px">Email</div>
  <div class="field abs" style="left:753px;top:139px;width:192px;height:38px">Phone</div>
  <div class="field abs" style="left:299px;top:216px;width:646px;height:98px;border-radius:49px;padding:26px 22px">Message</div>
  <a class="btn btn-red submit abs" href="#" style="font-size:18px">SUBMIT DETAILS</a>
</section>

<footer class="site-footer">
  <div class="foot-brand abs">Claim<br>Barrier<br>Plan</div>
  <span class="social abs" style="left:117px"></span>
  <span class="social abs" style="left:164px"></span>
  <span class="social abs" style="left:212px"></span>
  <span class="social abs" style="left:261px"></span>

  <h4 class="foot-head abs" style="left:478px">QUICK LINKS</h4>
  <a class="foot-link abs" style="top:150px;left:481px;color:#fff;text-decoration:none">Home</a>
  <a class="foot-link abs" style="top:193px;left:480px;color:#fff;text-decoration:none">About</a>
  <a class="foot-link abs" style="top:236px;color:#fff;text-decoration:none">Services</a>
  <a class="foot-link abs" style="top:281px;color:#fff;text-decoration:none">Contact Us</a>

  <h4 class="foot-head abs" style="left:838px">CONTACT INFO</h4>
  <div class="foot-info abs" style="top:157px"><span class="foot-icon"><svg width="16" height="16" viewBox="0 0 24 24"><path fill="#a51c38" d="M6.6 10.8a15 15 0 0 0 6.6 6.6l2.2-2.2a1 1 0 0 1 1-.25 11.4 11.4 0 0 0 3.6.57 1 1 0 0 1 1 1V20a1 1 0 0 1-1 1A17 17 0 0 1 3 4a1 1 0 0 1 1-1h3.5a1 1 0 0 1 1 1c0 1.25.2 2.45.57 3.6a1 1 0 0 1-.25 1z"/></svg></span><span style="margin-top:6px">(480) 555-0173</span></div>
  <div class="foot-info abs" style="top:208px"><span class="foot-icon"><svg width="16" height="16" viewBox="0 0 24 24"><path fill="#a51c38" d="M6.6 10.8a15 15 0 0 0 6.6 6.6l2.2-2.2a1 1 0 0 1 1-.25 11.4 11.4 0 0 0 3.6.57 1 1 0 0 1 1 1V20a1 1 0 0 1-1 1A17 17 0 0 1 3 4a1 1 0 0 1 1-1h3.5a1 1 0 0 1 1 1c0 1.25.2 2.45.57 3.6a1 1 0 0 1-.25 1z"/></svg></span><span style="margin-top:6px">(800) 555-0119</span></div>
  <div class="foot-info abs" style="top:266px"><span class="foot-icon"><svg width="16" height="16" viewBox="0 0 24 24"><path fill="#a51c38" d="M12 2a7 7 0 0 0-7 7c0 5 7 13 7 13s7-8 7-13a7 7 0 0 0-7-7zm0 9.5A2.5 2.5 0 1 1 12 6.5a2.5 2.5 0 0 1 0 5z"/></svg></span><span style="margin-top:2px">4820 NORTH SAGUARO WAY, SUITE 210,<br>MESA RIDGE, ARIZONA 85990</span></div>

  <div class="foot-rule abs"></div>
  <p class="copyright abs">Copyright © 2021. All rights reserved.</p>
</footer>

</body>
</html>
```